Delcourt Realty Business Cards

Design business card

Target Market(s)

High-End Buyer of Real Estate over $1 million dollars

Industry/Entity Type

Realtor

Contact Information for Business Card

Lena Delcourt R(S) LIC.# 41972
Cell 555 246-1938
Email Lena@Delcourt.example
Website IsleFreshHomes.example

Also Need Cards for:

Hank Delcourt R(B) LIC# 69418
C 555 613-7052
E Hank@Delcourt.example
W IsleFreshHomes.example

Colors

Designer to choose colors to be used in the design.

Requirements
Must have
• Address on back:
• 287 Pohaku Cir. , Wailea HI 96753
• Logo on back
Nice to have
• I would like the phone numbers and email address to be big so people can read it easily
Should not have
• Very small print Except For: address (287 Pohaku Cir. Wailea HI 96753)

```html
<!DOCTYPE html>
<html lang="en">
<head>
<meta charset="utf-8">
<title>Delcourt Realty Business Cards</title>
<link href="https://fonts.googleapis.com/css2?family=Open+Sans:wght@400;600;700&display=swap" rel="stylesheet">
<style>
  :root {
    --stage: #2b2a2a;
    --card-black: #0a0a0b;
    --card-white: #fbfbfa;
    --ink: #111111;
    --silver: #b9b9bb;
    --address: #b0b0b2;
    --photo-top: #c98a5e;
    --photo-bottom: #d8336f;
  }
  * { box-sizing: border-box; margin: 0; padding: 0; }
  html, body {
    width: 1200px; height: 1200px; overflow: hidden;
    background: var(--stage);
    font-family: "Open Sans", Arial, sans-serif;
  }
  .card {
    position: absolute; left: 220px;
    width: 760px; height: 434px;
    box-shadow: 0 10px 28px rgba(0,0,0,0.45);
  }
  /* Back of card */
  .card-back { top: 96px; background: var(--card-black); color: var(--silver); }
  .back-brand {
    position: absolute; left: 0; right: 0; top: 150px;
    display: flex; align-items: center; justify-content: center; gap: 22px;
  }
  .brand-square { width: 62px; height: 62px; background: var(--silver); }
  .back-brand .brand-name {
    font-size: 44px; font-weight: 600; letter-spacing: 5px; line-height: 1.05;
    text-transform: uppercase;
  }
  .back-address {
    position: absolute; left: 0; right: 0; bottom: 44px;
    text-align: center; font-size: 17px; letter-spacing: 1px;
    color: var(--address); text-transform: uppercase;
  }
  /* Front of card */
  .card-front { top: 620px; background: var(--card-white); color: var(--ink); overflow: hidden; }
  .front-brand {
    position: absolute; left: 50px; top: 70px; width: 160px;
    display: flex; flex-direction: column; align-items: center; gap: 18px;
  }
  .front-brand .brand-square { background: var(--ink); width: 70px; height: 70px; }
  .front-brand .brand-name {
    font-size: 24px; font-weight: 600; letter-spacing: 3px; line-height: 1.35;
    text-align: center; text-transform: uppercase; color: var(--ink);
  }
  .divider {
    position: absolute; left: 240px; top: 50px;
    width: 3px; height: 330px; background: var(--ink);
  }
  .agent { position: absolute; left: 272px; top: 52px; }
  .agent-name {
    font-size: 30px; font-weight: 700; letter-spacing: 1.5px;
    text-transform: uppercase; margin-bottom: 26px;
  }
  .contact-line { font-size: 24px; line-height: 36px; letter-spacing: 0.5px; }
  .contact-line b { font-weight: 700; }
  .website { font-size: 22px; letter-spacing: 0.5px; margin-top: 22px; }
  .agent-photo {
    position: absolute; right: 0; bottom: 0; width: 210px; height: 210px;
    background: linear-gradient(180deg, var(--photo-top) 0%, var(--photo-top) 55%, var(--photo-bottom) 100%);
  }
</style>
</head>
<body>
  <section class="card card-back">
    <div class="back-brand">
      <span class="brand-square"></span>
      <span class="brand-name">Delcourt<br>Realty</span>
    </div>
    <p class="back-address">287 Pohaku Cir. , Wailea HI 96753</p>
  </section>

  <section class="card card-front">
    <div class="front-brand">
      <span class="brand-square"></span>
      <span class="brand-name">Delcourt<br>Realty</span>
    </div>
    <div class="divider"></div>
    <div class="agent">
      <h1 class="agent-name">Lena Delcourt R(S)</h1>
      <p class="contact-line">LIC.# 41972</p>
      <p class="contact-line"><b>[C]</b> 555 246-1938</p>
      <p class="contact-line"><b>[E]</b> Lena@Delcourt.example</p>
      <p class="website">IsleFreshHomes.example</p>
    </div>
    <div class="agent-photo" role="img" aria-label="Portrait photo of the agent, smiling, in a pink top"></div>
  </section>
</body>
</html>
```